Combining web page

We need a PSD webpage design for our PrestaShop store that shows food combining rules, you can see an example that we put here, you can follow the same information and food image combinations. You are just doing the design but the images when implemented on the website will be clickable that goes to product categories, all text and images will be editable.

This is just an example:
http://merrowtonic.com/content/7-food-combining-rules

Target Market(s)

Natural Product and supplement industry

Industry/Entity Type

Store

Number of Pages Required

1 page

Colors

Designer to choose colors to be used in the design.

Requirements
Must have
• 1. Clear images.
• 2. Clear readable text.
• 3. Company name shown Merrow Tonic.
• 4. Follow the food rules as seen on the web page example, but not the same design.
• 5. Logo should be seen.
• 7. All text and images will be editable.
• 8. Make sure the food images are in their proper groups.
• 9. You are not coping the design we gave you but the details have to be the same, copy the text and the image food groups are important, you cannot just put any food in a group, and the combinations are important.
Nice to have
• Here is the website it is for http://merrowtonic.com/

```html
<!DOCTYPE html>
<html lang="en">
<head>
<meta charset="utf-8">
<title>Food Combining Rules – Merrow Tonic</title>
<link rel="stylesheet" href="https://fonts.googleapis.com/css2?family=Merriweather:wght@400;700&family=Oswald:wght@500;600&family=Roboto+Condensed:wght@400;700&display=swap">
<style>
:root{
  --page:#ececea;
  --paper:#f4f1ea;
  --panel:#f6f5f2;
  --white:#ffffff;
  --ink:#222222;
  --text:#444444;
  --muted:#777777;
  --line:#9a9a9a;
  --grid:#dddad3;
  --black:#111111;
  --green:#7cb342;
  --leaf:#4f8a2b;
  --price:#6aa12f;
  --orange:#e59a2b;
}
*{box-sizing:border-box;margin:0;padding:0}
html,body{width:1200px;height:3010px;overflow:hidden}
body{position:relative;background:var(--page);font-family:"Merriweather",Georgia,serif;color:var(--text)}
.abs{position:absolute}
.photo{position:absolute}

/* header */
.site-header{left:0;top:0;width:1200px;height:262px;background:linear-gradient(#f7f4ee,#efe9de);border-bottom:1px solid #ddd4c4}
.tagline{left:0;width:1200px;top:50px;text-align:center;font-size:13px;font-weight:700;letter-spacing:.5px;color:#333}
.search{left:172px;top:92px;width:218px;height:26px;border-bottom:1px solid #999;font-size:11px;color:#999;font-style:italic;padding-top:6px}
.search svg{position:absolute;right:2px;top:2px}
.brand{left:450px;top:86px;width:300px;text-align:center;white-space:nowrap}
.brand .mark{display:inline-block;width:20px;height:20px;background:var(--leaf);vertical-align:middle;margin-right:8px}
.brand .name{font-size:24px;font-weight:700;color:var(--leaf);vertical-align:middle}
.brand .sub{display:block;font-size:8px;color:#555;margin-top:4px}
.login{left:966px;top:50px;font-size:13px;color:#333}
.cart{left:926px;top:100px;font-size:15px;color:var(--green)}
.cart svg{vertical-align:-3px;margin-right:8px}
.main-nav{left:0;width:1200px;top:187px;display:flex;justify-content:center;gap:42px;font-size:13px;letter-spacing:.6px;color:#333}
.leaves{background:radial-gradient(circle at 40% 40%,#8cc152,#4f8a2b 70%,transparent 72%)}

.breadcrumb{left:0;width:1200px;top:270px;text-align:center;font-size:13px;color:#444}

/* main */
.main{left:88px;top:306px;width:1018px;height:2318px;background:var(--white)}
.sidebar{left:114px;top:336px;width:230px}
.bar{position:absolute;left:0;width:230px;height:36px;background:var(--black);color:#fff;font-size:13px;padding:11px 0 0 16px}
.side-menu{position:absolute;left:4px;top:56px;width:222px;list-style:none;font-size:12px;color:#333}
.side-menu li{height:25px;position:relative}
.side-menu li span{position:absolute;right:2px}
.product{position:absolute;left:0;width:230px;height:80px}
.product .thumb{position:absolute;left:4px;top:0;width:70px;height:70px;background:#fff;border:1px solid #eee}
.product .thumb i{position:absolute;left:16px;top:18px;width:38px;height:36px;border-radius:50%}
.product .title{position:absolute;left:86px;top:0;width:144px;font-size:11px;line-height:20px;color:#333}
.product .price{position:absolute;left:86px;font-size:11px;color:var(--price)}
.product .price s{color:#888;margin-left:8px}
.product .price em{font-style:normal;color:#999;margin-left:8px;font-size:10px}
.btn{position:absolute;left:116px;width:108px;height:34px;border-radius:17px;background:#333;color:#fff;font-size:11px;text-align:center;padding-top:10px}

.content{left:364px;top:328px;width:726px}
.page-title{font-size:17px;color:var(--ink);font-weight:700}
.panel{left:364px;top:370px;width:726px;height:2120px;background:var(--panel)}
.made-easy{left:364px;top:420px;width:726px;text-align:center;font-family:"Oswald",Impact,sans-serif;font-weight:600;font-size:26px;color:#555;letter-spacing:.5px}
.food-grid{left:408px;top:468px;width:680px;display:grid;grid-template-columns:repeat(3,1fr);grid-template-rows:repeat(3,146px)}
.food-cell{border-right:1px solid var(--grid);border-bottom:1px solid var(--grid);position:relative;text-align:center;font-family:"Roboto Condensed",Arial,sans-serif;font-size:11px;color:#333}
.food-cell:nth-child(3n){border-right:none}
.food-cell:nth-child(n+7){border-bottom:none}
.food-cell .img{width:130px;height:84px;margin:12px auto 8px;border-radius:45%}
.grid-caption{left:364px;width:726px;top:928px;text-align:center;font-family:"Roboto Condensed",Arial,sans-serif;font-weight:700;font-size:13px;color:#333}

.rules{left:386px;top:956px;width:704px;border-collapse:collapse;font-family:"Roboto Condensed",Arial,sans-serif;background:var(--white);table-layout:fixed}
.rules td,.rules th{border:1px solid var(--line);text-align:center;vertical-align:middle;color:#333}
.rules .num{height:22px;font-size:15px;font-weight:400}
.rules .colname{font-size:10px;line-height:12px;height:96px;font-weight:400;vertical-align:middle}
.rules .key{text-align:left;font-size:11px;font-weight:700;padding-left:12px;line-height:15px;vertical-align:middle}
.rules .label{text-align:left;vertical-align:top;padding:10px 8px}
.rules .label b{display:block;font-size:13px;font-weight:400;color:#222;margin-bottom:6px}
.rules .label .lorem{display:flex;gap:16px;font-size:10px;line-height:13px;color:#666}
.rules td.v{font-size:14px;font-weight:700}
.rules td.v small{display:block;font-size:8px;font-weight:400;color:#777;line-height:9px}

.principles-title{left:364px;width:726px;top:2294px;text-align:center;font-size:19px;font-weight:700;color:#444}
.principles{left:384px;top:2338px;width:690px;display:grid;grid-template-columns:repeat(4,minmax(0,1fr));gap:24px;font-family:"Roboto Condensed",Arial,sans-serif;font-size:11px;line-height:19px;color:#444}
.principles p{min-width:0;overflow-wrap:anywhere;word-break:break-all}

/* footer */
.site-footer{left:0;top:2640px;width:1200px;height:370px;background:linear-gradient(#f3efe6,#ebe5d8)}
.social{left:548px;top:2710px;display:flex;gap:10px}
.social i{display:block;width:24px;height:24px;border-radius:50%;background:#222}
.footer-links{left:120px;width:960px;top:2756px;text-align:center;font-size:11px;line-height:22px;color:#333}
.footer-links span{margin:0 6px;color:#666}
.subscribe{left:438px;top:2824px;width:324px;height:40px;border:1px solid #bbb;border-radius:20px;background:#fff}
.subscribe b{position:absolute;right:-1px;top:-1px;width:106px;height:40px;border-radius:0 20px 20px 0;background:#222;color:#fff;font-size:11px;font-weight:400;text-align:center;padding-top:13px}
.note{left:0;width:1200px;top:2878px;text-align:center;font-size:10px;line-height:22px;color:var(--green)}
.copyright{left:0;width:1200px;top:2926px;text-align:center;font-size:12px;color:#333}
.to-top{left:1128px;top:2930px;width:32px;height:32px;border-radius:50%;background:var(--green)}
</style>
</head>
<body>

<!-- side produce -->
<div class="photo" role="img" aria-label="Sliced lemons" style="left:0;top:330px;width:88px;height:450px;background:radial-gradient(circle at 20% 50%,#fbe27a,#f1c232 60%,#e9ecd8 100%)"></div>
<div class="photo" role="img" aria-label="Green cabbage" style="left:0;top:1520px;width:88px;height:400px;background:radial-gradient(circle at 10% 50%,#b9d88a,#6a9b3a 60%,#e4e8dc 100%)"></div>
<div class="photo" role="img" aria-label="Fresh mango" style="left:1106px;top:820px;width:94px;height:460px;background:radial-gradient(circle at 90% 50%,#f6b43a,#d9542b 55%,#e9e6dc 100%)"></div>
<div class="photo" role="img" aria-label="Orange and mango slices with splash" style="left:1106px;top:1800px;width:94px;height:420px;background:radial-gradient(circle at 90% 50%,#f7a324,#e8622a 55%,#e9e6dc 100%)"></div>

<!-- header -->
<header class="abs site-header">
  <div class="abs leaves" role="img" aria-label="Ivy leaves" style="left:0;top:0;width:140px;height:262px;opacity:.85"></div>
  <div class="abs leaves" role="img" aria-label="Ivy leaves" style="left:1060px;top:0;width:140px;height:262px;opacity:.85"></div>
  <div class="abs tagline">ANCIENT FOODS FOR TODAYS LIFESTYLE</div>
  <div class="abs search">Search
    <svg width="20" height="20" viewBox="0 0 20 20"><circle cx="8" cy="8" r="6" fill="none" stroke="#333" stroke-width="1.6"/><line x1="12.5" y1="12.5" x2="18" y2="18" stroke="#333" stroke-width="1.8"/></svg>
  </div>
  <div class="abs brand"><span class="mark"></span><span class="name">Merrow Tonic</span><span class="sub">Ancient Foods For Today's People</span></div>
  <div class="abs login">Login ⌄</div>
  <div class="abs cart"><svg width="22" height="20" viewBox="0 0 22 20"><path d="M1 2h4l3 11h10l3-8H7" fill="none" stroke="#555" stroke-width="1.6"/><circle cx="9" cy="17" r="1.6" fill="#555"/><circle cx="17" cy="17" r="1.6" fill="#555"/></svg>(0 Cart)</div>
  <nav class="abs main-nav"><span>OUR PRODUCTS</span><span>INGREDIENTS</span><span>HEALTH CONCERNS</span><span>OUR BLOGS</span><span>MORE</span></nav>
</header>

<div class="abs breadcrumb">Home &nbsp;|&nbsp; Food Combining Rules</div>

<main class="abs main"></main>

<!-- sidebar -->
<aside class="abs sidebar">
  <div class="bar" style="top:0">Home</div>
  <ul class="side-menu">
    <li>Our Products<span>+</span></li>
    <li>Ingredients<span>+</span></li>
    <li>Health Concerns</li>
    <li>Edible Legumes</li>
    <li>Asparagus</li>
    <li>Cauliflower</li>
    <li>Cabbages<span>+</span></li>
  </ul>
  <div class="abs" role="img" aria-label="Fresh vegetables in a wicker basket" style="left:0;top:274px;width:230px;height:264px;background:radial-gradient(circle at 50% 45%,#c98f4a,#7fae4a 55%,#f7f7f2 85%)"></div>

  <div class="bar" style="top:566px">Best Sellers</div>
  <div class="product" style="top:624px"><div class="thumb"><i style="background:#e9a13b"></i></div><div class="title">The Adventure Begins Framed...</div><div class="price" style="top:46px">$29.00</div></div>
  <div class="product" style="top:716px"><div class="thumb"><i style="background:#d8442f"></i></div><div class="title">Mountain Fox Notebook</div><div class="price" style="top:46px">$12.90</div></div>
  <div class="product" style="top:812px"><div class="thumb"><i style="background:#e9c13b"></i></div><div class="title">Hummingbird Printed Sweater</div><div class="price" style="top:46px">$28.72<s>$35.90</s><em>-20%</em></div></div>
  <div class="btn" style="top:920px">All Products</div>

  <div class="bar" style="top:998px">Featured Products</div>
  <div class="product" style="top:1058px"><div class="thumb"><i style="background:#b9d36a"></i></div><div class="title">Hummingbird Printed T-shirt</div><div class="price" style="top:46px">$19.12<s>$23.90</s><em>-20%</em></div></div>
  <div class="product" style="top:1154px"><div class="thumb"><i style="background:#e9c13b"></i></div><div class="title">Hummingbird Printed Sweater</div><div class="price" style="top:46px">$28.72<s>$35.90</s><em>-20%</em></div></div>
  <div class="product" style="top:1250px"><div class="thumb"><i style="background:#e9a13b"></i></div><div class="title">The Best Is Yet To Come'...</div><div class="price" style="top:46px">$29.00</div></div>
  <div class="btn" style="top:1352px">All Products</div>

  <div class="bar" style="top:1428px">New Products</div>
  <div class="product" style="top:1488px"><div class="thumb"><i style="background:#d9653a"></i></div><div class="title">Customizable Mug</div><div class="price" style="top:26px">$13.69<s>$13.90</s><em>-2%</em></div></div>
  <div class="product" style="top:1584px"><div class="thumb"><i style="background:#8bbf4a"></i></div><div class="title">Hummingbird Notebook</div><div class="price" style="top:46px">$12.75<s>$12.90</s><em>-1%</em></div></div>
  <div class="product" style="top:1684px"><div class="thumb"><i style="background:#9ccc5a"></i></div><div class="title">Brown Bear Notebook</div><div class="price" style="top:26px">$12.64<s>$12.90</s><em>-2%</em></div></div>
  <div class="btn" style="top:1800px">All Products</div>

  <div class="bar" style="top:1860px">Special Products</div>
  <div class="product" style="top:1922px"><div class="thumb"><i style="background:#e9c13b"></i></div><div class="title">Hummingbird Printed Sweater</div><div class="price" style="top:46px">$28.72<s>$35.90</s><em>-20%</em></div></div>
  <div class="product" style="top:2020px"><div class="thumb"><i style="background:#b9d36a"></i></div><div class="title">Hummingbird Printed T-shirt</div><div class="price" style="top:46px">$19.12<s>$23.90</s><em>-20%</em></div></div>
  <div class="product" style="top:2116px"><div class="thumb"><i style="background:#d9653a"></i></div><div class="title">Customizable Mug</div><div class="price" style="top:26px">$13.69<s>$13.90</s><em>-2%</em></div></div>
  <div class="btn" style="top:2214px">All Products</div>
</aside>

<!-- content -->
<div class="abs content"><h1 class="page-title">Food Combining Rules</h1></div>
<section class="abs panel"></section>
<h2 class="abs made-easy">FOOD COMINING MADE EASY</h2>

<div class="abs food-grid">
  <div class="food-cell"><div class="img" role="img" aria-label="Citrus fruits: grapefruit, orange, lemon, lime" style="background:radial-gradient(circle,#f6c945,#ef7d3a)"></div>1. CITRUS - ACID FOOD</div>
  <div class="food-cell"><div class="img" role="img" aria-label="Sub acid fruits: apples, berries, grapes" style="background:radial-gradient(circle,#e44a3a,#7a4a8a)"></div>2. FRUITS (Sub Acid)</div>
  <div class="food-cell"><div class="img" role="img" aria-label="Sweet and palm fruits: banana, pineapple, coconut" style="background:radial-gradient(circle,#f3cf45,#8a6a3a)"></div>3. SWEET &amp; PALM FRUIT</div>
  <div class="food-cell"><div class="img" role="img" aria-label="Raw nuts and seeds" style="background:radial-gradient(circle,#c69a62,#7a5a34)"></div>3. NEUTRAL FRUITS<br>RAW NUTS &amp; SEED</div>
  <div class="food-cell"><div class="img" role="img" aria-label="Sack of grains" style="background:radial-gradient(circle,#e6cf9c,#a88150)"></div>5. GRAINS</div>
  <div class="food-cell"><div class="img" role="img" aria-label="Legumes and sprouts" style="background:radial-gradient(circle,#d8a35a,#8a3a2a)"></div>6. LEGUMES SPROUTS</div>
  <div class="food-cell"><div class="img" role="img" aria-label="Melons: cantaloupe, honeydew, watermelon" style="background:radial-gradient(circle,#f6b86a,#5a8a3a)"></div>7. MELONS</div>
  <div class="food-cell"><div class="img" role="img" aria-label="Basket of tomatoes and succulent foods" style="background:radial-gradient(circle,#e2512f,#7f9a3a)"></div>8. SUCCULENT FOOD TOMATES</div>
  <div class="food-cell"><div class="img" role="img" aria-label="Mixed fresh vegetables" style="background:radial-gradient(circle,#7fb443,#d8483a)"></div>3. VEGETABLES</div>
</div>
<div class="abs grid-caption">9. Succulent Food Tematoes</div>

<table class="abs rules">
  <colgroup><col style="width:280px"><col span="9" style="width:47px"></colgroup>
  <tr><th class="key" rowspan="2">Key : &nbsp;XX Combines Well<br>&emsp;&emsp;&nbsp;X Fair Compatibility<br><br>&emsp;&emsp;&nbsp;NR Not Recommended<br>&emsp;&emsp;&nbsp;NO Not Compatible</th>
    <th class="num">1</th><th class="num">2</th><th class="num">3</th><th class="num">4</th><th class="num">5</th><th class="num">6</th><th class="num">7</th><th class="num">8</th><th class="num">9</th></tr>
  <tr><th class="colname">Citrus Acid Food</th><th class="colname">Fruits Sub Acid</th><th class="colname">Sweet Plam Fruits</th><th class="colname">Neutral Fruits Raw Nuts Seed</th><th class="colname">Grains</th><th class="colname">Legum-es Sprouts</th><th class="colname">Melons</th><th class="colname">Succul-ent Food Tomato-es</th><th class="colname">Veget-ables</th></tr>

  <tr style="height:104px"><td class="label"><b>1. Citrus Acid Food</b><div class="lorem"><span>Lorem<br>Ipsum<br>Dolor<br>Amet</span><span>Lorem<br>Ipsum<br>Dolor<br>Amet</span><span>Lorem<br>Ipsum<br>Dolor<br>Amet</span></div></td>
    <td class="v">XX</td><td class="v">XX</td><td class="v"><small>XX sit XX lorem XX sit</small>X</td><td class="v">XX</td><td class="v">NR<small>XX sit XX lorem XX sit</small></td><td class="v">X-NR<small>XX sit XX lore</small></td><td class="v">X<small>XX sit XX lore</small></td><td class="v">NO</td><td class="v">NO</td></tr>

  <tr style="height:132px"><td class="label"><b>2. Fruits Sub Acid</b><div class="lorem"><span>Lorem<br>Ipsum<br>Dolor<br>Amet</span><span>Lorem<br>Ipsum<br>Dolor<br>Amet</span><span>Lorem<br>Ipsum<br>Dolor<br>Amet</span><span>Lorem<br>Ipsum<br>Dolor<br>Sit<br>Amet<br>Connect</span><span>Lorem<br>Ipsum<br>Dolor<br>Amet<br>Sit<br>Connect</span></div></td>
    <td class="v">XX</td><td class="v">XX</td><td class="v"><small>XX sit XX lorem XX sit</small>X</td><td class="v">XX</td><td class="v">NR<small>XX sit XX lorem XX sit</small></td><td class="v">X-NR<small>XX sit XX lore</small></td><td class="v">X<small>XX sit XX lore</small></td><td class="v">NO</td><td class="v">NO</td></tr>

  <tr style="height:100px"><td class="label"><b>3. Sweet Fruits Plan Fruits</b><div class="lorem"><span>Lorem<br>Ipsum<br>Dolor<br>Amet</span><span>Lorem<br>Ipsum<br>Dolor<br>Amet</span><span>Lorem<br>Ipsum<br>Dolor<br>Sit</span></div></td>
    <td class="v">XX</td><td class="v">XX</td><td class="v"><small>XX sit XX lorem XX sit</small>X</td><td class="v">XX</td><td class="v">NR<small>XX sit XX lorem XX sit</small></td><td class="v">X-NR<small>XX sit XX lore</small></td><td class="v">X<small>XX sit XX lore</small></td><td class="v">NO</td><td class="v">NO</td></tr>

  <tr style="height:124px"><td class="label"><b>4. Neutral Fruits Raw Nut Seed</b><div class="lorem"><span>Lorem<br>Ipsum<br>Dolor<br>Amet</span><span>Lorem<br>Ipsum<br>Dolor<br>Amet</span><span>Lorem<br>Ipsum<br>Dolor<br>Sit<br>Amet</span><span>Lorem<br>Ipsum<br>Dolor<br>Sit<br>Amet</span><span>Lorem<br>Ipsum<br>Dolor<br>Sit<br>Amet</span></div></td>
    <td class="v">XX</td><td class="v">XX</td><td class="v">XX</td><td class="v">XX</td><td class="v">XX</td><td class="v">XX</td><td class="v">XX</td><td class="v">X</td><td class="v">XX</td></tr>

  <tr style="height:100px"><td class="label"><b>5. Grains</b><div class="lorem"><span>Lorem<br>Ipsum<br>Dolor<br>Amet</span><span>Lorem<br>Ipsum<br>Dolor<br>Amet</span><span>Lorem<br>Ipsum<br>Dolor<br>Amet</span></div></td>
    <td class="v"><small>XX sit XX lorem</small>NR</td><td class="v">XX</td><td class="v">XX</td><td class="v">XX</td><td class="v">XX</td><td class="v">X-NR</td><td class="v">XX</td><td class="v">XX</td><td class="v">XX</td></tr>

  <tr style="height:118px"><td class="label"><b>6. Legumes Sprouts</b><div class="lorem"><span>Lorem<br>Ipsum<br>Dolor<br>Amet</span><span>Lorem<br>Ipsum<br>Dolor<br>Amet</span><span>Lorem<br>Ipsum<br>Dolor<br>Amet</span><span>Lorem<br>Ipsum<br>Dolor<br>Sit<br>Amet</span><span>Lorem<br>Ipsum<br>Dolor<br>Sit<br>Amet</span></div></td>
    <td class="v"><small>XX sit XX lorem</small>X-NR</td><td class="v">XX</td><td class="v"><small>XX sit XX lorem</small>NO<small>XX sit</small></td><td class="v">XX</td><td class="v">XX</td><td class="v">XX</td><td class="v">NR</td><td class="v">XX</td><td class="v"><small>XX sit</small>XX</td></tr>

  <tr style="height:102px"><td class="label"><b>7. Melons</b><div class="lorem"><span>Lorem<br>Ipsum<br>Dolor<br>Amet</span><span>Lorem<br>Ipsum<br>Dolor<br>Amet</span><span>Lorem<br>Ipsum<br>Dolor<br>Amet</span></div></td>
    <td class="v">X</td><td class="v"><small>XX sit XX lorem</small>X</td><td class="v">X_NR</td><td class="v">X</td><td class="v">X_NR</td><td class="v">NR</td><td class="v">XX</td><td class="v">NA</td><td class="v">NO</td></tr>

  <tr style="height:206px"><td class="label"><b>8. Succulent Food Tomatoes</b><div class="lorem"><span>Lorem<br>Ipsum<br>Dolor<br>Amet<br>Dolor<br>Amet</span><span>Lorem<br>Ipsum<br>Dolor<br>Amet<br>Dolor<br>Amet</span><span>Lorem<br>Ipsum<br>Dolor<br>Amet<br>Dolor<br>Amet<br>Dolor<br>Amet</span><span>Lorem<br>Ipsum<br>Dolor<br>Amet<br>Dolor<br>Sit<br>Amet</span><span>Lorem<br>Ipsum<br>Dolor<br>Amet<br>Dolor<br>Amet<br>Dolor<br>Amet</span></div></td>
    <td class="v"><small>XX sit</small>X-NR</td><td class="v"><small>XX sit XX lorem</small>X-NR</td><td class="v"><small>XX sit XX lorem</small>XX</td><td class="v">XX</td><td class="v">XX</td><td class="v">XX</td><td class="v">NR</td><td class="v">XX</td><td class="v"><small>XX sit</small>XX</td></tr>

  <tr style="height:204px"><td class="label"><b>9. Vegetables</b><div class="lorem"><span>Lorem<br>Ipsum<br>Dolor<br>Amet<br>Dolor<br>Amet<br>Dolor<br>Amet</span><span>Lorem<br>Ipsum<br>Dolor<br>Amet<br>Dolor<br>Amet<br>Dolor<br>Amet</span><span>Lorem<br>Ipsum<br>Dolor<br>Amet<br>Dolor<br>Amet<br>Dolor<br>Amet</span><span>Lorem<br>Ipsum<br>Dolor<br>Amet<br>Dolor<br>Amet<br>Dolor<br>Amet</span><span>Lorem<br>Ipsum<br>Dolor<br>Amet<br>Dolor<br>Amet<br>Dolor<br>Amet</span></div></td>
    <td class="v"><small>XX sit</small>X-NR</td><td class="v"><small>XX sit XX lorem</small>X-NR</td><td class="v"><small>XX sit XX lorem</small>NO<small>XX sit</small></td><td class="v">XX</td><td class="v">XX</td><td class="v">XX</td><td class="v">NR</td><td class="v">XX</td><td class="v"><small>XX sit</small>XX</td></tr>
</table>

<h3 class="abs principles-title">Principles of Eating</h3>
<div class="abs principles">
  <p>make a typespecimenbook. Ithassurvivednotonlyfivecenturies,utalsotheleaptoelectronictypesetting,remainingessentialllunchanged.Lorem Ipsum imply dummy text of the printing</p>
  <p>make a typespecimenbook. Ithassurvivednotonlyfivecenturies,utalsotheleaptoelectronictypesetting,remainingessentialllunchanged.Lorem Ipsum imply dummy text of the printing</p>
  <p>make a typespecimenbook. Ithassurvivednotonlyfivecenturies,utalsotheleaptoelectronictypesetting,remainingessentialllunchanged.Lorem Ipsum imply dummy text of the printing</p>
  <p>make a typespecimenbook. Ithassurvivednotonlyfivecenturies,utalsotheleaptoelectronictypesetting,remainingessentialllunchanged.Lorem Ipsum imply dummy text of the printing</p>
</div>

<!-- footer -->
<footer class="abs site-footer">
  <div class="abs leaves" role="img" aria-label="Climbing ivy" style="left:80px;top:0;width:150px;height:340px;opacity:.8"></div>
  <div class="abs leaves" role="img" aria-label="Climbing ivy" style="left:980px;top:0;width:170px;height:340px;opacity:.8"></div>
</footer>
<div class="abs social"><i></i><i></i><i></i></div>
<div class="abs footer-links">Delivery<span>|</span>Legal Notice<span>|</span>Terms And Conditions Of Use<span>|</span>About Us<span>|</span>Secure Payment<span>|</span>Food Combining Rules<span>|</span>TODD COMBINING<br><span>|</span>Todd CSS CODE<span>|</span>Contact Us<span>|</span>Sitemap<span>|</span>Stores</div>
<div class="abs subscribe"><b>SUBSCRIBE</b></div>
<div class="abs note">You May Unsubscribe At Any Moment. For That Purpose,<br>Please Find Our Contact Info In The Legal Notice.</div>
<div class="abs copyright">© 2017 Ecommerce site powered by Leafline Studio</div>
<div class="abs to-top"><svg width="32" height="32" viewBox="0 0 32 32"><path d="M10 19l6-6 6 6" fill="none" stroke="#fff" stroke-width="2"/></svg></div>

</body>
</html>
```